Business cards - Yoga Instructor
Quiet Fern Yoga
Creative Brief
Use same font as used in my logo
Use fonts that you feel work well with the logo and style of card
Bright & Fun-filled
Miriam Tovbrask
Certified Yoga Instructor
Austin, Texas
mtovbrask@brightpost.example
www.Quietfern.example
The front should include the "Quiett Fern Yoga" logo that we have uploaded. Also - we would like to include "Offering Veyolin based yoga" on the card as well. perhaps just below the title "Certified Yoga Instructor"
we would like to have the "Ohm" symbol on the back of the card and the words "Strength - Stability - Freedom". here is a link for a sample of the symbol. http://www.breathwheelsite.example/ok.htm We are thinking the Ohm symbol can fill the entire back (even going off the edges) and the text on top.

```html
<!DOCTYPE html>
<html lang="en">
<head>
<meta charset="utf-8">
<title>Miriam Tovbrask – Yoga Instructor Business Cards</title>
<link href="https://fonts.googleapis.com/css2?family=Source+Sans+3:ital,wght@0,400;0,600;1,400;1,700&display=swap" rel="stylesheet">
<style>
  :root {
    --board: #8f8f8f;
    --board-light: #a3a3a3;
    --title: #ffffff;
    --purple: #8a4f9e;
    --purple-soft: #b58ac4;
    --pink: #d9579c;
    --ink: #5b5b5b;
    --white: #ffffff;
    --back-blue-a: #7d71b8;
    --back-blue-b: #a99bd4;
    --back-pink-a: #c667b0;
    --back-pink-b: #e3a4d3;
    --back-lav-a: #9f72b8;
    --back-lav-b: #c4a5d6;
  }
  * { box-sizing: border-box; margin: 0; padding: 0; }
  html, body { width: 1200px; height: 888px; overflow: hidden; }
  body {
    font-family: "Source Sans 3", "Myriad Pro", sans-serif;
    background: radial-gradient(ellipse at 50% 45%, var(--board-light), var(--board) 75%);
    position: relative;
  }
  .board-title {
    position: absolute; left: 113px; top: 16px;
    color: var(--title); font-style: italic; line-height: 1.15;
  }
  .board-title h1 { font-size: 22px; font-weight: 700; }
  .board-title p { font-size: 15px; font-weight: 400; }

  .card {
    position: absolute;
    border-radius: 12px; overflow: hidden;
    box-shadow: 0 3px 8px rgba(0,0,0,.35);
  }
  .option-label {
    position: absolute; z-index: 5; width: 28px; height: 28px; border-radius: 50%;
    background: #e9e9e9; color: #444; font-size: 11px; font-weight: 600;
    display: flex; align-items: center; justify-content: center;
    box-shadow: 0 1px 2px rgba(0,0,0,.3);
  }

  /* Front */
  .card-front { left: 113px; top: 168px; width: 463px; height: 276px; background: var(--white); }
  .front-band {
    position: absolute; left: 0; right: 0; bottom: 0; height: 24px;
    background: linear-gradient(90deg, var(--purple-soft), var(--purple));
  }
  .wordmark {
    position: absolute; left: 0; right: 0; top: 60px; text-align: center;
    color: var(--pink); font-size: 38px; font-weight: 400; letter-spacing: .5px;
  }
  .wordmark-dot {
    display: inline-block; width: 12px; height: 12px; border-radius: 50%;
    background: var(--pink); margin-left: 8px; vertical-align: 14px;
  }
  .instructor { position: absolute; left: 48px; width: 230px; top: 176px; text-align: center; color: var(--ink); }
  .instructor .name { color: var(--purple); font-size: 21px; font-weight: 400; line-height: 1.1; }
  .instructor .role { font-size: 12px; margin-top: 2px; }
  .instructor .offer { color: var(--purple); font-style: italic; font-size: 12px; margin-top: 12px; }
  .divider { position: absolute; left: 264px; top: 176px; width: 1px; height: 68px; background: #c9b6d2; }
  .contacts { position: absolute; left: 278px; top: 172px; list-style: none; font-size: 11px; color: var(--ink); }
  .contacts li { display: flex; align-items: center; height: 19px; }
  .contacts svg { width: 12px; height: 12px; margin-right: 7px; flex: none; }

  /* Backs */
  .card-back .om-area {
    position: absolute; left: 150px; top: -30px; width: 300px; height: 340px;
    border-radius: 45%;
    background: radial-gradient(ellipse at 50% 45%, rgba(255,255,255,.22), rgba(255,255,255,.05) 70%);
  }
  .card-back .sheen {
    position: absolute; inset: 0;
    background: linear-gradient(160deg, rgba(255,255,255,.15), rgba(255,255,255,0) 45%);
  }
  .card-back .motto {
    position: absolute; left: 48px; top: 158px;
    color: var(--white); font-size: 22px; font-style: italic; font-weight: 400; white-space: nowrap;
  }
  .back-blue { left: 612px; top: 139px; width: 461px; height: 281px; background: linear-gradient(135deg, var(--back-blue-b), var(--back-blue-a)); }
  .back-pink { left: 96px; top: 487px; width: 473px; height: 293px; background: linear-gradient(135deg, var(--back-pink-a), var(--back-pink-b) 60%, var(--back-pink-a)); }
  .back-pink .motto { left: 58px; top: 152px; }
  .back-lavender { left: 612px; top: 480px; width: 461px; height: 283px; background: linear-gradient(135deg, var(--back-lav-b), var(--back-lav-a)); }
  .back-lavender .motto { top: 154px; }
</style>
</head>
<body>
  <header class="board-title">
    <h1>Miriam Tovbrask</h1>
    <p>Yoga Instructor - Business cards</p>
  </header>

  <span class="option-label" style="left:116px;top:142px">5a</span>
  <span class="option-label" style="left:622px;top:142px">12a</span>
  <span class="option-label" style="left:106px;top:490px">12b</span>
  <span class="option-label" style="left:622px;top:486px">12c</span>

  <section class="card card-front">
    <div class="wordmark">Quiet Fern Yoga<span class="wordmark-dot"></span></div>
    <div class="instructor">
      <div class="name">Miriam Tovbrask</div>
      <div class="role">Certified Yoga Instructor</div>
      <div class="offer">Offering Veyolin based yoga</div>
    </div>
    <div class="divider"></div>
    <ul class="contacts">
      <li><svg viewBox="0 0 12 12"><circle cx="6" cy="6" r="6" fill="#8a4f9e"/><path d="M6 2.5a2 2 0 0 0-2 2c0 1.6 2 4.5 2 4.5s2-2.9 2-4.5a2 2 0 0 0-2-2z" fill="#fff"/></svg>Austin, Texas</li>
      <li><svg viewBox="0 0 12 12"><circle cx="6" cy="6" r="6" fill="#8a4f9e"/><path d="M4 3h1.2l.6 1.6-.8.6a4 4 0 0 0 1.8 1.8l.6-.8L9 6.8V8a1 1 0 0 1-1 1A5 5 0 0 1 3 4a1 1 0 0 1 1-1z" fill="#fff"/></svg>(512) 555-0148</li>
      <li><svg viewBox="0 0 12 12"><circle cx="6" cy="6" r="6" fill="#8a4f9e"/><rect x="3" y="4" width="6" height="4" fill="#fff"/><path d="M3 4l3 2.2L9 4" stroke="#8a4f9e" stroke-width=".7" fill="none"/></svg>mtovbrask@brightpost.example</li>
      <li><svg viewBox="0 0 12 12"><circle cx="6" cy="6" r="6" fill="#8a4f9e"/><circle cx="6" cy="6" r="3" fill="none" stroke="#fff" stroke-width=".8"/><path d="M3 6h6M6 3v6" stroke="#fff" stroke-width=".6"/></svg>www.Quietfern.example</li>
    </ul>
    <div class="front-band"></div>
  </section>

  <section class="card card-back back-blue">
    <div class="om-area" role="img" aria-label="Large faint Om symbol filling the card"></div>
    <div class="sheen"></div>
    <p class="motto">Strength · Stability · Freedom</p>
  </section>

  <section class="card card-back back-pink">
    <div class="om-area" role="img" aria-label="Large faint Om symbol filling the card"></div>
    <div class="sheen"></div>
    <p class="motto">Strength · Stability · Freedom</p>
  </section>

  <section class="card card-back back-lavender">
    <div class="om-area" role="img" aria-label="Large faint Om symbol filling the card"></div>
    <div class="sheen"></div>
    <p class="motto">Strength · Stability · Freedom</p>
  </section>
</body>
</html>
```